Letterhead, stationery and email signature for construction business

I need the letterhead, stationery and email signature designs for a construction business. I want them to have a corporate feel to them.

I've attached the logo for reference.

```html
<!DOCTYPE html>
<html lang="en">
<head>
<meta charset="utf-8">
<title>Bramford Builders Letterhead</title>
<link rel="stylesheet" href="https://fonts.googleapis.com/css2?family=Lato:wght@400;700&family=Figtree:wght@600;700&family=Great+Vibes&display=swap">
<style>
  :root {
    --backdrop: #e3e3e3;
    --paper: #ffffff;
    --paper-edge: #eeeeee;
    --brand-blue: #2d54a0;
    --brand-blue-light: #2f63ab;
    --steel: #5a5c68;
    --steel-light: #7a7d88;
    --ink: #333333;
    --ink-strong: #2a2a2a;
  }
  * { margin: 0; padding: 0; box-sizing: border-box; }
  html, body {
    width: 1153px; height: 1200px; overflow: hidden;
    background: var(--backdrop);
  }
  .letterhead {
    position: absolute; left: 170px; top: 30px;
    width: 814px; height: 1140px;
    background: radial-gradient(ellipse at 55% 35%, var(--paper) 0%, var(--paper) 30%, var(--paper-edge) 100%);
    box-shadow: 0 6px 24px rgba(0,0,0,0.18);
    overflow: hidden;
    font-family: "Lato", sans-serif;
    color: var(--ink);
  }
  .brand {
    position: absolute; left: 74px; top: 74px;
    display: flex; align-items: center; gap: 12px;
  }
  .brand-mark { width: 44px; height: 44px; background: var(--brand-blue); }
  .brand-name {
    font-family: "Lato", sans-serif; font-weight: 700;
    font-size: 31px; color: var(--brand-blue); letter-spacing: 0.5px;
  }
  .contact {
    position: absolute; left: 555px; top: 50px; height: 94px;
    border-left: 1.5px solid var(--brand-blue);
    padding-left: 7px;
    font-style: normal;
    font-family: "Figtree", sans-serif; font-weight: 700;
    font-size: 13.5px; line-height: 17.5px; color: var(--ink-strong);
  }
  .contact-address { margin-bottom: 8px; }
  .contact-line { display: flex; align-items: center; gap: 6px; height: 19px; }
  .contact-line svg { width: 13px; height: 13px; fill: var(--brand-blue); flex: none; }
  .letter-body {
    position: absolute; left: 63px; top: 252px; width: 689px;
    font-size: 15.6px; line-height: 17.5px;
  }
  .date { margin-bottom: 20px; }
  .recipient { margin-bottom: 20px; }
  .salutation {
    font-size: 19px; font-weight: 700; color: var(--ink-strong);
    margin: 24px 0 22px;
  }
  .paragraph { text-align: justify; margin-bottom: 17px; }
  .closing { margin-top: 38px; }
  .signature {
    font-family: "Great Vibes", cursive; font-size: 40px;
    color: var(--ink-strong); margin-top: 24px; margin-left: 3px;
  }
  .footer-rule {
    position: absolute; left: 0; bottom: 92px; width: 814px; height: 8px;
    background: linear-gradient(90deg, var(--steel-light), var(--steel) 50%, var(--steel-light));
  }
  .footer-band {
    position: absolute; left: 0; bottom: 0; width: 814px; height: 84px;
    background: linear-gradient(90deg, var(--brand-blue), var(--brand-blue-light) 50%, var(--brand-blue));
  }
</style>
</head>
<body>
  <main class="letterhead">
    <header>
      <div class="brand">
        <span class="brand-mark"></span>
        <span class="brand-name">Bramford Builders</span>
      </div>
      <address class="contact">
        <div class="contact-address">42-10 Harbor Lane 5,<br>Westbrook, NY 11402</div>
        <div class="contact-line">
          <svg viewBox="0 0 16 16" aria-hidden="true"><path d="M3 2h3l1.5 3.5-2 1.3a9 9 0 0 0 3.7 3.7l1.3-2L14 10v3a1 1 0 0 1-1 1A12 12 0 0 1 2 3a1 1 0 0 1 1-1z"/></svg>
          <span>555-204-7781</span>
        </div>
        <div class="contact-line">
          <svg viewBox="0 0 16 16" aria-hidden="true"><path d="M1 3h14v10H1z M2 4.2v.3l6 4 6-4v-.3z" fill-rule="evenodd"/></svg>
          <span>info@bramfordbuild.com</span>
        </div>
        <div class="contact-line">
          <svg viewBox="0 0 16 16" aria-hidden="true"><circle cx="8" cy="8" r="7"/><path d="M1 8h14M8 1c3 3 3 11 0 14M8 1c-3 3-3 11 0 14" stroke="#fff" stroke-width="1" fill="none"/></svg>
          <span>www.bramfordbuild.com</span>
        </div>
      </address>
    </header>

    <section class="letter-body">
      <p class="date">Feb-03-2022</p>
      <p class="recipient">Mr, John Doe<br>President</p>
      <p class="recipient">Alder Corporation<br>123 Street Name, Suite# 10<br>City, State, 120023</p>
      <p class="salutation">Dear Mr, John</p>
      <p class="paragraph">Lorem ipsum dolor sit amet, consectetur adipisicing elit, sed do eiusmod tempor incididunt ut labore et dolore magna aliqua. Ut enim ad minim veniam, quis nostrud exercitation ullamco laboris nisi ut aliquip ex ea commodo consequat. Duis aute irure dolor in reprehenderit in voluptate velit esse cillum dolore eu fugiat nulla pariatur.</p>
      <p class="paragraph">Lorem ipsum dolor sit amet, consectetur adipisicing elit, sed do eiusmod tempor incididunt ut labore et dolore magna aliqua. Ut enim ad minim veniam, quis nostrud exercitation ullamco laboris nisi ut aliquip ex ea commodo consequat. Duis aute irure dolor in reprehenderit in voluptate velit esse cillum dolore eu fugiat nulla pariatur.</p>
      <p class="paragraph">Lorem ipsum dolor sit amet, consectetur adipisicing elit, sed do eiusmod tempor incididunt ut labore et dolore magna aliqua. Ut enim ad minim veniam, quis nostrud exercitation ullamco laboris nisi ut aliquip ex ea commodo consequat.</p>
      <p class="paragraph">Excepteur sint occaecat cupidatat non proident, sunt in culpa qui officia deserunt mollit anim id est laborum. re et dolore magnam aliquam quaerat voluptatem.</p>
      <p class="closing">Regards</p>
      <p class="signature">Daniel Hart</p>
    </section>

    <footer>
      <div class="footer-rule"></div>
      <div class="footer-band"></div>
    </footer>
  </main>
</body>
</html>
```